Mosk trail Website

We need a simple web page design for our businessWe procure and dispose of earthmoving construction equipmentwe also find construction equipment for our customers using our global contacts

Number of Pages Required

1 page

```html
<!DOCTYPE html>
<html lang="en">
<head>
<meta charset="utf-8">
<title>Mosk trail</title>
<link rel="stylesheet" href="https://fonts.googleapis.com/css2?family=Montserrat:wght@400;600;700&family=Open+Sans:wght@400;600&family=Playfair+Display:ital@1&display=swap">
<style>
:root{
  --canvas:#ffffff;
  --page:#262626;
  --footer:#1e1e1e;
  --orange:#f4a52a;
  --white:#ffffff;
  --muted:#d6d6d6;
  --line:#8a8a8a;
  --card-border:#6f6f6f;
  --field:#ffffff;
}
*{box-sizing:border-box;margin:0;padding:0}
html,body{width:1200px;height:2885px;overflow:hidden;background:var(--canvas)}
body{font-family:"Open Sans",Arial,sans-serif;color:var(--white)}
.page{position:absolute;left:110px;top:77px;width:980px;height:2745px;background:var(--page);overflow:hidden}
.abs{position:absolute}
.section-title{position:absolute;left:0;width:980px;text-align:center;font-family:"Montserrat",Arial,sans-serif;font-weight:700;font-size:28px;letter-spacing:3px}

/* hero */
.hero{left:0;top:0;width:980px;height:426px;background:radial-gradient(ellipse at 52% 42%,#c98a22 0%,#7a5216 28%,#3a2a10 58%,#1c1a14 100%)}
.brand{left:78px;top:22px;font-family:"Montserrat",Arial,sans-serif;font-weight:600;font-size:17px;color:var(--white)}
.nav{right:78px;top:25px;display:flex;gap:20px;font-family:"Montserrat",Arial,sans-serif;font-size:10.5px;letter-spacing:.8px;color:var(--white)}
.hero-kicker{left:0;width:980px;top:225px;text-align:center;font-family:"Playfair Display",Georgia,serif;font-style:italic;font-size:29px;letter-spacing:1px}
.hero-title{left:0;width:980px;top:262px;text-align:center;font-family:"Montserrat",Arial,sans-serif;font-weight:700;font-size:50px;letter-spacing:2px}
.hero-btn{left:411px;top:357px;width:158px;height:34px;border:1.5px solid var(--white);border-radius:18px;text-align:center;line-height:31px;font-family:"Montserrat",Arial,sans-serif;font-size:11px;letter-spacing:1.5px}
.arrow{top:196px;font-size:14px;color:#bbb}

/* services */
.service{width:420px;text-align:center}
.service-icon{display:block;margin:0 auto;width:76px;height:76px}
.service h3{margin-top:12px;font-family:"Montserrat",Arial,sans-serif;font-weight:700;font-size:15px;letter-spacing:2px}
.service p{margin-top:5px;font-size:11px}

/* about */
.about-photo{left:75px;top:809px;width:403px;height:234px;border-radius:8px;background:radial-gradient(ellipse at 38% 40%,#f3c75a 0%,#c4761c 18%,#5a3a14 45%,#161616 80%)}
.about-text{left:501px;top:811px;width:403px;font-size:10px;line-height:14px;color:var(--muted)}
.about-text p+p{margin-top:8px}
.about-rule{left:501px;top:1012px;width:403px;border-top:1px solid var(--line)}
.btn{background:var(--orange);color:var(--white);font-family:"Montserrat",Arial,sans-serif;font-size:11.5px;text-align:center;border-radius:2px}

/* equipment */
.card{top:1194px;width:267px;height:367px;border:1px solid var(--card-border);border-radius:5px;overflow:hidden;text-align:center}
.card-photo{height:106px;background:radial-gradient(ellipse at 50% 20%,#f7c55a 0%,#d18a25 28%,#6b4513 60%,#1a1a1a 100%)}
.badge{position:absolute;left:50%;width:58px;height:58px;margin-left:-29px;border-radius:50%;background:var(--white);color:var(--orange);font-family:"Montserrat",Arial,sans-serif;font-weight:700;display:flex;align-items:center;justify-content:center;text-align:center}
.card .badge{top:92px;font-size:9px;line-height:10px;letter-spacing:1px}
.card h4{margin-top:50px;font-family:"Montserrat",Arial,sans-serif;font-weight:700;font-size:16px;line-height:17px;letter-spacing:2px}
.card .blurb{margin:8px 16px 0;font-family:"Montserrat",Arial,sans-serif;font-weight:700;font-size:9px;line-height:11.5px;letter-spacing:1.4px;color:var(--orange)}
.card .contact{margin-top:10px;font-size:10.5px;line-height:16px}

/* testimonial */
.testimonial{left:0;top:1639px;width:980px;height:257px;background:linear-gradient(180deg,#5a4426 0%,#2a231a 30%,#1f1f1f 50%,#2b2620 72%,#4b3d2a 100%)}
.avatar{left:466px;top:54px;width:48px;height:48px;border-radius:50%;background:#2f8f8c}
.quote{left:130px;top:128px;width:720px;text-align:center;font-size:12.5px;line-height:20px}
.quote b{font-family:Georgia,serif;font-size:22px;vertical-align:-4px}
.client{left:0;width:980px;top:174px;text-align:center;font-size:10px;color:var(--muted)}
.stars{left:460px;top:190px}
.dots{left:466px;top:210px;display:flex;gap:6px}
.dots span{width:7px;height:7px;border-radius:50%;border:1px solid #bbb}
.dots span.on{background:#fff;border-color:#fff}

/* team */
.member{left:288px;top:1954px;width:403px;height:242px;border:1px solid var(--card-border);border-radius:5px;overflow:hidden;text-align:center}
.member .card-photo{height:120px}
.member .badge{top:102px;font-size:16px}
.member h4{margin-top:34px;font-family:"Montserrat",Arial,sans-serif;font-weight:700;font-size:17px;letter-spacing:2px}
.member .role{margin-top:4px;font-family:"Montserrat",Arial,sans-serif;font-weight:700;font-size:9.5px;letter-spacing:1.8px;color:var(--orange)}
.member .contact{margin-top:5px;font-size:10.5px;line-height:16px}

/* contact */
.touch{left:75px;top:2356px;width:403px}
.touch h3{font-family:"Montserrat",Arial,sans-serif;font-weight:700;font-size:17px;letter-spacing:2px}
.touch p{margin-top:6px;font-size:10.5px;line-height:15px;color:var(--muted)}
.info-row{position:absolute;left:75px;width:403px;border-bottom:1px solid var(--line);font-size:10px;line-height:15.5px}
.info-row svg{position:absolute;left:0;top:0}
.info-row .txt{margin-left:38px}
.form{left:501px;top:2362px;width:403px}
.form label{display:block;font-size:10px;font-weight:600;height:14px}
.field{height:22px;background:var(--field);border-radius:2px;margin-bottom:13px;color:#9a9a9a;font-size:10px;padding:5px 8px}
.field.message{height:96px}

/* footer */
.footer{left:0;top:2694px;width:980px;height:51px;background:var(--footer);font-size:10px;color:var(--muted)}
.footer .copy{position:absolute;left:75px;top:18px}
.footer .social{position:absolute;right:75px;top:21px;display:flex;gap:14px}
.footer .social span{width:8px;height:8px;border-radius:50%;background:var(--muted)}
</style>
</head>
<body>
<main class="page">

  <header class="abs hero" role="img" aria-label="Photo of a bulldozer silhouetted against a sunset, under a faint grid overlay"></header>
  <div class="abs brand">Mosk trail</div>
  <nav class="abs nav"><span>ABOUT</span><span>SERVICES</span><span>TESTIMONIALS</span><span>WHO</span><span>EQUIPMENT FOR SALE</span><span>CONTACT</span></nav>
  <span class="abs arrow" style="left:74px">&#8249;</span>
  <span class="abs arrow" style="right:74px">&#8250;</span>
  <div class="abs hero-kicker">WELCOME TO</div>
  <h1 class="abs hero-title">MOSK TRAIL</h1>
  <div class="abs hero-btn">CONTACT US</div>

  <h2 class="section-title" style="top:460px">OUR SERVICES</h2>
  <div class="abs service" style="left:69px;top:546px">
    <svg class="service-icon" viewBox="0 0 76 76"><circle cx="38" cy="38" r="38" fill="#f4a52a"/><path d="M25 32c0-3 2-5 4-5h2v-3c0-2 2-3 3.5-3s3.5 1 3.5 3v-1c0-2 2-3 3.5-3s3.5 1 3.5 3v2c0-2 2-3 3.5-3S52 23 52 25v15c0 8-5 14-13 14h-1c-7 0-13-5-13-12z" fill="none" stroke="#fff" stroke-width="3" stroke-linejoin="round"/><path d="M31 27v9M38 23v12M45 24v11" stroke="#fff" stroke-width="2.5"/></svg>
    <h3>WE PROCURE AND DISPOSE</h3>
    <p>We procure and dispose of earthmoving construction equipment</p>
  </div>
  <div class="abs service" style="left:490px;top:546px">
    <svg class="service-icon" viewBox="0 0 76 76"><circle cx="38" cy="38" r="38" fill="#f4a52a"/><circle cx="34" cy="34" r="13" fill="none" stroke="#fff" stroke-width="4"/><path d="M43 43l12 12" stroke="#fff" stroke-width="6" stroke-linecap="round"/><path d="M34 27v14M27 34h14" stroke="#fff" stroke-width="3.5"/></svg>
    <h3>FIND CONSTRUCTION EQUIPMENTS</h3>
    <p>We also find construction equipment for our customers using our global contacts</p>
  </div>

  <h2 class="section-title" style="top:746px">ABOUT US</h2>
  <div class="abs about-photo" role="img" aria-label="Photo of an excavator silhouetted against the setting sun"></div>
  <div class="abs about-text">
    <p>Lorem ipsum dolor sit amet, consectetur adipiscing elit. Donec a tempor eros. Pellentesque elementum nulla sed justo tempor posuere sit amet sit amet ligula. Curabitur felis nibh, imperdiet eu erat non, luctus cursus lectus. Donec maximus diam leo, sed fringilla nisl auctor eget. Donec dictum neque est, ac faucibus ex blandit a. Curabitur felis nibh, imperdiet eu erat non, luctus cursus lectus. Donec maximus diam leo, sed fringilla nisl auctor eget. Donec dictum neque est, ac faucibus ex blandit a.</p>
    <p>Lorem ipsum dolor sit amet, consectetur adipiscing elit. Donec a tempor eros. Pellentesque elementum nulla sed justo tempor posuere sit amet sit amet ligula. Curabitur felis nibh, imperdiet eu erat non, luctus cursus lectus. Donec maximus diam leo, sed fringilla nisl auctor eget. Donec dictum neque est, ac faucibus ex blandit a.</p>
  </div>
  <div class="abs about-rule"></div>
  <div class="abs btn" style="left:501px;top:1035px;width:104px;height:29px;line-height:29px">CONTACT US</div>

  <h2 class="section-title" style="top:1131px">EQUIPMENTS FOR SALE</h2>
  <article class="abs card" style="left:66px">
    <div class="card-photo" role="img" aria-label="Photo of a bulldozer silhouetted at sunset"></div>
    <div class="badge">FOR<br>SALE</div>
    <h4>NAME OF<br>EQUEPEMENT</h4>
    <p class="blurb">LOREM IPSUM DOLOR SIT AMET, CONSECTETUR SUNT ELIT. IMPEDIT ISTE PERSPICIATIS EARUM VOLUPTATEM AD POSSIMUS ITAQUE, EUM ASPERNATUR, NOSTRUM DIGNISSIMOS BEATAE ID IN ILLUM ACCUSANTIUM ADIPISICING SUSCIPIT SUNT DOLOREMQUE.</p>
    <p class="contact">Contact For Rate And more details:<br>dale@mosktrail.com.au<br>0412 555 018</p>
  </article>
  <article class="abs card" style="left:356px">
    <div class="card-photo" role="img" aria-label="Photo of a bulldozer silhouetted at sunset"></div>
    <div class="badge">FOR<br>SALE</div>
    <h4>NAME OF<br>EQUEPEMENT</h4>
    <p class="blurb">LOREM IPSUM DOLOR SIT AMET, CONSECTETUR SUNT ELIT. IMPEDIT ISTE PERSPICIATIS EARUM VOLUPTATEM AD POSSIMUS ITAQUE, EUM ASPERNATUR, NOSTRUM DIGNISSIMOS BEATAE ID IN ILLUM ACCUSANTIUM ADIPISICING SUSCIPIT SUNT DOLOREMQUE.</p>
    <p class="contact">Contact For Rate And more details:<br>dale@mosktrail.com.au<br>0412 555 018</p>
  </article>
  <article class="abs card" style="left:646px">
    <div class="card-photo" role="img" aria-label="Photo of a bulldozer silhouetted at sunset"></div>
    <div class="badge">FOR<br>SALE</div>
    <h4>NAME OF<br>EQUEPEMENT</h4>
    <p class="blurb">LOREM IPSUM DOLOR SIT AMET, CONSECTETUR SUNT ELIT. IMPEDIT ISTE PERSPICIATIS EARUM VOLUPTATEM AD POSSIMUS ITAQUE, EUM ASPERNATUR, NOSTRUM DIGNISSIMOS BEATAE ID IN ILLUM ACCUSANTIUM ADIPISICING SUSCIPIT SUNT DOLOREMQUE.</p>
    <p class="contact">Contact For Rate And more details:<br>dale@mosktrail.com.au<br>0412 555 018</p>
  </article>

  <section class="abs testimonial" role="img" aria-label="Dim photo band of earthmoving machines silhouetted at dusk">
    <div class="abs avatar" role="img" aria-label="Client avatar illustration"></div>
    <p class="abs quote"><b>&ldquo;</b> Lorem ipsum dolor sit amet, ea sea dolore ubique, duo consul nominavi eu. Illum partem vidisse no vix. Id unum scribentur est. Posse luptatum vituperatoribus et quo, usu cu veri nominavi scripserit, eum cu natum iuvaret. <b>&rdquo;</b></p>
    <div class="abs client">Rhys Calder</div>
    <svg class="abs stars" width="60" height="12" viewBox="0 0 60 12"><g fill="#f4c20d"><path id="st" d="M6 0l1.8 3.8 4.2.5-3.1 2.8.8 4.1L6 9.2 2.3 11.2l.8-4.1L0 4.3l4.2-.5z"/><use href="#st" x="12"/><use href="#st" x="24"/><use href="#st" x="36"/><path d="M54 0l1.8 3.8 0 5.4L54 9.2V0z" transform="translate(-6 0)"/></g></svg>
    <div class="abs dots"><span></span><span></span><span class="on"></span><span></span></div>
  </section>

  <article class="abs member">
    <div class="card-photo" role="img" aria-label="Photo of a bulldozer silhouetted at sunset"></div>
    <div class="badge">MT</div>
    <h4>DALE HARKER</h4>
    <p class="role">MANAGING DIRECTOR</p>
    <p class="contact">dale@mosktrail.com.au<br>0412 555 018</p>
  </article>

  <h2 class="section-title" style="top:2285px">CONTACT US</h2>
  <div class="abs touch">
    <h3>GET IN TOUCH</h3>
    <p>Lorem ipsum dolor sit amet, consectetur adipiscing elit. Curabitur eget leo at velit imperdiet varius. In eu ipsum vitae velit congue iaculis vitae at risus. Lorem ipsum dolor sit amet, consectetur adipiscing elit.</p>
  </div>
  <div class="info-row" style="top:2443px;border-top:1px solid var(--line);padding:12px 0 8px;height:108px">
    <svg width="14" height="18" viewBox="0 0 14 18" style="top:10px"><path d="M7 0a7 7 0 0 1 7 7c0 5-7 11-7 11S0 12 0 7a7 7 0 0 1 7-7z" fill="#f4a52a"/><circle cx="7" cy="7" r="2.6" fill="#262626"/></svg>
    <div class="txt">ADDRESS</div>
    <div>Address line one<br>Address line two<br>Address line two<br>Address line two</div>
  </div>
  <div class="info-row" style="top:2551px;height:46px;padding-top:20px">
    <svg width="18" height="16" viewBox="0 0 18 16" style="top:17px"><rect width="18" height="16" rx="2" fill="#f4a52a"/><path d="M5 3c1 0 2 2 2 3s-1 1-1 2 2 3 3 3 1-1 2-1 3 1 3 2-1 2-2 2C7 14 4 9 4 5c0-1 0-2 1-2z" fill="#262626"/></svg>
    <div class="txt">0412 555 018</div>
  </div>
  <div class="info-row" style="top:2597px;height:45px;padding-top:18px">
    <svg width="20" height="14" viewBox="0 0 20 14" style="top:17px"><rect width="20" height="14" rx="1.5" fill="#f4a52a"/><path d="M1 1l9 7 9-7" fill="none" stroke="#262626" stroke-width="1.6"/></svg>
    <div class="txt">dale@mosktrail.com.au</div>
  </div>

  <form class="abs form">
    <label>Name:</label><div class="field">Enter name</div>
    <label>Email:</label><div class="field">Enter email</div>
    <label>Subject:</label><div class="field">Enter subject</div>
    <label>Message:</label><div class="field message">Enter message</div>
    <div class="btn" style="width:112px;height:29px;line-height:29px;font-family:'Open Sans',Arial,sans-serif;font-size:12px">Send Message</div>
  </form>

  <footer class="abs footer">
    <span class="copy">&copy; 2018 @MoskTrail.</span>
    <div class="social"><span></span><span></span><span></span><span></span></div>
  </footer>

</main>
</body>
</html>
```